New business Card Design

I'm looking to do a new design for our business cards.

Our Company its called the Lantern quarter we are a High end outdoor Design and construction company based out of miami FL

Our Style is elegant, minimalist, Luxury but accessible.

see our Website: www.thelanternquarter.example

Attached find our logo as well as some samples the cards that we have for our sister company.

Sample Contact information ( in no particular order):

Marco Bettancur
VP of Sales and Marketing
Marco@thelanternquarter.example
786.402.9158
4712 NW 63 AVE Miami Florida, 33166
Updates

Designs are Looking Great guys but not quite there yet!

Upload your last few designs between today and Tomorrow. we will be choosing one on Saturday!

Cheers, 

Marco Bettancur
Director Of Marketing 

Hello Guys, 

Sorry we have not made a decision yet.  a lot of cool stuff! just narrowing down our options. 
expect a decision with in a day or 2. 

Marco. 

Target Market(s)

high End Design and construction. Luxurious but accessible

Industry/Entity Type

Construction

Colors

Designer to choose colors to be used in the design.

```html
<!DOCTYPE html>
<html lang="en">
<head>
<meta charset="utf-8">
<title>The Lantern Quarter – Business Card</title>
<link rel="stylesheet" href="https://fonts.googleapis.com/css2?family=Open+Sans:wght@400;600;700&display=swap">
<style>
  :root {
    --bg: #e9e8e6;
    --card-white: #ffffff;
    --green-light: #8fd275;
    --green: #5cbc4a;
    --green-deep: #3aa43a;
    --blue: #3f5fb8;
    --ink: #222222;
    --ink-soft: #3a3a3a;
    --brand-grey: #4a4a4a;
  }
  * { margin: 0; padding: 0; box-sizing: border-box; }
  html, body {
    width: 1200px; height: 800px; overflow: hidden;
    background: var(--bg);
    font-family: "Open Sans", Arial, sans-serif;
  }
  .stage { position: relative; width: 1200px; height: 800px; }

  /* Back of card */
  .card-back {
    position: absolute; left: 110px; top: 138px;
    width: 300px; height: 525px;
    background: linear-gradient(160deg, var(--green-deep) 0%, var(--green) 50%, var(--green-light) 100%);
    box-shadow: 0 10px 28px rgba(0,0,0,.22);
    overflow: hidden;
  }
  .card-back .arcs { position: absolute; inset: 0; }
  .card-back .brand-mark {
    position: absolute; left: 34px; top: 34px;
    width: 46px; height: 46px; border-radius: 50%;
    background: var(--card-white); opacity: .9;
  }
  .card-back .brand-name {
    position: absolute; left: 44px; top: 96px;
    writing-mode: vertical-rl;
    font-size: 27px; font-weight: 600; letter-spacing: 2px;
    color: var(--ink); text-transform: uppercase; white-space: nowrap;
  }

  /* Front of card */
  .card-front {
    position: absolute; left: 470px; top: 222px;
    width: 620px; height: 354px;
    background: var(--card-white);
    box-shadow: 0 10px 28px rgba(0,0,0,.22);
    overflow: hidden;
  }
  .card-front .swoosh { position: absolute; inset: 0; }
  .brand {
    position: absolute; left: 250px; top: 30px;
    display: flex; align-items: center; gap: 12px;
  }
  .brand-name-front {
    font-size: 20px; font-weight: 600; letter-spacing: 1px;
    color: var(--brand-grey); text-transform: uppercase; white-space: nowrap;
  }
  .brand-dot {
    width: 48px; height: 48px; border-radius: 50%;
    background: var(--green); flex: none;
  }
  .person { position: absolute; left: 385px; top: 96px; }
  .person-name { font-size: 17px; font-weight: 700; color: var(--ink); letter-spacing: .3px; white-space: nowrap; }
  .person-title { font-size: 14px; color: var(--ink-soft); margin-top: 1px; white-space: nowrap; }

  .contacts {
    position: absolute; left: 40px; top: 108px;
    list-style: none; font-size: 12.5px; color: var(--ink);
  }
  .contacts li { display: flex; align-items: center; gap: 8px; margin-bottom: 7px; white-space: nowrap; }
  .contacts svg { width: 14px; height: 14px; flex: none; }

  .address {
    position: absolute; left: 360px; top: 292px;
    font-size: 14px; line-height: 1.45; color: var(--ink); font-style: normal; white-space: nowrap;
  }
</style>
</head>
<body>
<main class="stage">

  <section class="card-back" aria-label="Card back">
    <svg class="arcs" viewBox="0 0 300 525" aria-hidden="true">
      <g fill="none" stroke="#ffffff" stroke-opacity=".18" stroke-width="14">
        <circle cx="-60" cy="620" r="300"/>
        <circle cx="-60" cy="620" r="420"/>
      </g>
    </svg>
    <span class="brand-mark" aria-hidden="true"></span>
    <p class="brand-name">The Lantern Quarter</p>
  </section>

  <section class="card-front" aria-label="Card front">
    <svg class="swoosh" viewBox="0 0 620 354" aria-hidden="true">
      <defs>
        <linearGradient id="swooshGreen" x1="0" y1="0" x2="1" y2="1">
          <stop offset="0" stop-color="#3aa43a"/>
          <stop offset=".55" stop-color="#8fd275"/>
          <stop offset="1" stop-color="#5cbc4a"/>
        </linearGradient>
      </defs>
      <path d="M0 40 C 250 60, 500 200, 600 354 L0 354 Z" fill="url(#swooshGreen)"/>
      <path d="M0 37 C 250 57, 502 197, 604 354" fill="none" stroke="#3f5fb8" stroke-width="5"/>
    </svg>

    <div class="brand">
      <span class="brand-name-front">The Lantern Quarter</span>
      <span class="brand-dot" aria-hidden="true"></span>
    </div>

    <div class="person">
      <p class="person-name">MARCO BETTANCUR</p>
      <p class="person-title">VP of Sales and Marketing</p>
    </div>

    <ul class="contacts">
      <li>
        <svg viewBox="0 0 14 14" aria-hidden="true"><circle cx="7" cy="7" r="7" fill="#222"/><path d="M4.5 3.8c.5-.3.9 0 1.1.5l.4.9c.1.3 0 .6-.3.8l-.4.3c.4.9 1 1.5 1.9 1.9l.3-.4c.2-.3.5-.4.8-.3l.9.4c.5.2.8.6.5 1.1-.4.8-1.2 1.1-2 .8C6 9.9 4.1 8 3.7 6 3.5 5.1 3.8 4.3 4.5 3.8z" fill="#fff"/></svg>
        786.402.9158
      </li>
      <li>
        <svg viewBox="0 0 14 14" aria-hidden="true"><circle cx="7" cy="7" r="7" fill="#222"/><rect x="3.5" y="4.5" width="7" height="5" rx=".6" fill="none" stroke="#fff" stroke-width="1"/><path d="M3.6 4.8 7 7.4l3.4-2.6" fill="none" stroke="#fff" stroke-width="1"/></svg>
        Marco@thelanternquarter.example
      </li>
    </ul>

    <address class="address">
      4712 NW 63 AVE<br>
      Miami Florida, 33166
    </address>
  </section>

</main>
</body>
</html>
```